Business Card Design Project

I own a dental practice and would like to use a logo that was recently designed to make business cards.
I am looking for a clean card with the following information on the card.

Halvorsen Dental Center (Using the logo)
Martin K. Halvorsen, D.D.S.
2847 Willow Bend Rd. Suite B
Colorado Springs, CO 80471
(719) 555-0186
halvorsendentalcenter@mailnest.example
www.halvorsendentalcenter.example

Also a list of items on the back:
Services include

Family Dentistry
Cosmetic
Whitening
Tooth Colored Fillings
Crowns/Bridges
Implants/Tooth Replacement
Dentures
Root Canals
Updates

Just an FYI, I added an email address and website address.

I also added my Pic.  Please give designs with and without the pic

Thanks

Target Market(s)

20-70 U.S. Female that handles the household budget.

Industry/Entity Type

Dental

Requirements
Must have
• The logo is key. The color scheme of the logo is also key. The back of the business card should have the list of Dental Services offered at the practice. The front should be clean and professional looking. No cartoons. I will also include a picture of myself. I think that the final card may or may not include this picture, so the card designs should come with and without the picture. USE THE BLUE LOGO ONLY!!!
Should not have
• NO teeth should be on the card.

```html
<!DOCTYPE html>
<html lang="en">
<head>
<meta charset="utf-8">
<title>Halvorsen Dental Center – Business Card</title>
<link rel="stylesheet" href="https://fonts.googleapis.com/css2?family=Montserrat:wght@400;500;600&display=swap">
<style>
  :root {
    --teal: #2a7b98;
    --teal-dark: #1f6681;
    --paper: #ffffff;
    --backdrop: #e6e8ea;
    --photo-a: #d9d2cc;
    --photo-b: #3a3f48;
  }
  * { box-sizing: border-box; margin: 0; padding: 0; }
  html, body { width: 1200px; height: 900px; overflow: hidden; }
  body {
    background: var(--backdrop);
    font-family: "Montserrat", sans-serif;
    position: relative;
  }
  .card {
    position: absolute;
    left: 250px;
    width: 700px;
    height: 400px;
    background: var(--paper);
    border-radius: 28px;
    overflow: hidden;
    box-shadow: 0 6px 18px rgba(0,0,0,0.18);
  }
  .card--back { top: 40px; }
  .card--front { top: 460px; }

  /* Back */
  .back-band { position: absolute; inset: 0; width: 100%; height: 100%; }
  .services {
    position: absolute;
    list-style: none;
    color: var(--teal);
    font-size: 17px;
    line-height: 1.5;
    white-space: nowrap;
  }
  .services li::before { content: "• "; }
  .services--left { left: 46px; top: 56px; }
  .services--right { left: 360px; top: 32px; }
  .back-brand {
    position: absolute;
    left: 60px;
    bottom: 66px;
    display: flex;
    align-items: center;
    gap: 18px;
  }
  .brand-dot {
    width: 48px; height: 48px;
    border-radius: 50%;
    background: var(--paper);
    opacity: 0.9;
  }
  .back-brand .brand-name {
    color: var(--paper);
    font-size: 34px;
    font-weight: 500;
  }

  /* Front */
  .front-brand {
    position: absolute;
    left: 44px;
    top: 60px;
    color: var(--teal);
    font-size: 32px;
    font-weight: 500;
    line-height: 1.15;
    width: 340px;
  }
  .doctor {
    position: absolute;
    left: 44px;
    top: 180px;
    color: var(--teal);
    font-size: 24px;
    font-weight: 500;
    white-space: nowrap;
  }
  .contact {
    position: absolute;
    left: 44px;
    top: 222px;
    list-style: none;
    color: var(--teal);
    font-size: 15px;
    line-height: 1.55;
    white-space: nowrap;
  }
  .contact .label {
    display: inline-block;
    width: 22px;
    font-weight: 600;
    color: var(--teal-dark);
  }
  .contact .address { display: flex; gap: 6px; margin-top: 6px; }
  .contact .address svg { flex: none; margin-top: 3px; }
  .portrait {
    position: absolute;
    right: 0;
    top: 30px;
    width: 260px;
    height: 340px;
    background: linear-gradient(180deg, var(--photo-a) 0%, #b9a9a0 40%, var(--photo-b) 75%);
  }
</style>
</head>
<body>

  <section class="card card--back" aria-label="Card back">
    <svg class="back-band" viewBox="0 0 700 400" preserveAspectRatio="none" aria-hidden="true">
      <path d="M0 255 C 250 240, 500 200, 700 145 L700 400 L0 400 Z" fill="#2a7b98"/>
      <path d="M380 252 C 520 220, 630 192, 700 172" fill="none" stroke="#ffffff" stroke-width="5"/>
    </svg>
    <ul class="services services--left">
      <li>Family Dentistry</li>
      <li>Cosmetic</li>
      <li>Whitening</li>
      <li>Tooth Colored Fillings</li>
    </ul>
    <ul class="services services--right">
      <li>Crowns/Bridges</li>
      <li>Implants/Tooth Replacement</li>
      <li>Dentures</li>
      <li>Root Canals</li>
    </ul>
    <div class="back-brand">
      <span class="brand-dot"></span>
      <span class="brand-name">Halvorsen Dental Center</span>
    </div>
  </section>

  <section class="card card--front" aria-label="Card front">
    <div class="front-brand">Halvorsen Dental Center</div>
    <p class="doctor">Martin K. Halvorsen, D.D.S.</p>
    <ul class="contact">
      <li><span class="label">p</span>(719) 555-0186</li>
      <li><span class="label">e</span>halvorsendentalcenter@mailnest.example</li>
      <li><span class="label">w</span>www.halvorsendentalcenter.example</li>
      <li class="address">
        <svg width="16" height="14" viewBox="0 0 16 14" aria-hidden="true">
          <path d="M8 0 L16 7 L13.5 7 L13.5 14 L9.5 14 L9.5 9.5 L6.5 9.5 L6.5 14 L2.5 14 L2.5 7 L0 7 Z" fill="#1f6681"/>
        </svg>
        <span>2847 Willow Bend Rd. Suite B<br>Colorado Springs, CO 80471</span>
      </li>
    </ul>
    <div class="portrait" role="img" aria-label="Portrait photo of the dentist in a dark suit"></div>
  </section>

</body>
</html>
```